Locksmith Security Services Flyer

I'm looking for a flyer to high light services I offer within the locksmith industry. I don't require all services on the flyer. but it would be nice if they can be put on there. Logo needs to be on there as well as contact number , website and email address, and if possible other pictures, I would like it bright but it needs to be professional and have the "Stalwart" Look

Target Market(s)

Property owners

Industry/Entity Type

Locksmith

Font styles to use
Serif
Sans Serif

Requirements
Must have
• Contact number : 0800 562 7093
Website : www.stalwartalliance.co.uk
Email : locksmith@stalwartalliance.co.uk
Nice to have
• Lock Changes
Lock Upgrades
Lock Outs
Master key system
Keyed Alike
Key Cutting
Board ups

```html
<!DOCTYPE html>
<html lang="en">
<head>
<meta charset="utf-8">
<title>Stalwart Partnership – Locksmith Services Flyer</title>
<link rel="stylesheet" href="https://fonts.googleapis.com/css2?family=Oswald:wght@500&family=PT+Sans+Narrow:wght@400;700&family=PT+Sans:wght@400;700&display=swap">
<style>
  :root{
    --stage:#2f2f31;
    --brand-blue:#1f4fb3;
    --brand-deep:#173c8f;
    --brand-light:#3f74d6;
    --ink:#1c1c22;
    --paper:#ffffff;
    --paper-tint:#eef2f9;
    --photo-a:#c9d6e4;
    --photo-b:#8fa67a;
  }
  *{box-sizing:border-box;margin:0;padding:0}
  html,body{width:1200px;height:800px;overflow:hidden;background:var(--stage)}
  .canvas{position:relative;width:1200px;height:800px}
  .flyer{
    position:absolute;left:324px;top:10px;width:596px;height:843px;
    transform:scale(0.925);transform-origin:top left;
    background:linear-gradient(180deg,var(--paper) 0%,var(--paper-tint) 55%,var(--paper) 100%);
    overflow:hidden;font-family:"PT Sans Narrow",Arial,sans-serif;color:var(--ink);
    box-shadow:0 6px 18px rgba(0,0,0,.35);
  }
  .header-art{position:absolute;left:0;top:0;width:596px;height:303px}
  .brand-mark{
    position:absolute;left:18px;top:44px;width:120px;display:flex;align-items:center;gap:6px;
    font-family:"PT Sans",Arial,sans-serif;font-weight:700;font-size:13px;line-height:1.1;color:var(--brand-blue);
  }
  .brand-mark .dot{width:14px;height:14px;border-radius:50%;background:var(--brand-blue);flex:none}
  .hero-title{
    position:absolute;left:25px;top:148px;font-family:"Oswald",Arial,sans-serif;font-weight:500;
    font-size:27px;letter-spacing:.2px;color:#fff;transform:scaleX(.86);transform-origin:left;
  }
  .hero-rule{position:absolute;left:25px;top:191px;width:60px;height:2px;background:#fff}
  .hero-intro{
    position:absolute;left:25px;top:206px;width:245px;color:#fff;font-family:"PT Sans",Arial,sans-serif;
    font-size:10px;line-height:13.4px;text-align:justify;
  }
  .service{position:absolute;width:260px;display:flex;gap:6px}
  .service .hex{flex:none;width:36px;height:40px}
  .service-body{width:215px}
  .service h3{font-family:"PT Sans",Arial,sans-serif;font-weight:700;font-size:10.5px;color:var(--brand-blue);line-height:12px;text-transform:uppercase;letter-spacing:-.1px}
  .service p{font-size:8.2px;line-height:10px;text-align:justify}
  .service .price{color:var(--brand-blue);margin-top:5px;text-align:left}
  .col-left{left:24px}
  .col-right{left:316px}
  .security-box{
    position:absolute;left:316px;top:637px;width:257px;height:128px;border-radius:3px;
    background:linear-gradient(135deg,var(--brand-light),var(--brand-blue) 55%,var(--brand-deep));
    color:#fff;padding:36px 16px 0 16px;
  }
  .security-tab{
    position:absolute;left:56px;top:-2px;width:146px;height:22px;background:#fff;
    clip-path:polygon(0 0,100% 0,96% 100%,4% 100%);
    display:flex;align-items:center;justify-content:center;
    font-family:"Oswald",Arial,sans-serif;font-weight:500;font-size:11px;color:var(--brand-blue);
  }
  .security-box .lead{font-size:8.2px;line-height:10.5px}
  .security-box .lead b{font-weight:700}
  .security-list{list-style:none;margin-top:8px}
  .security-list li{display:flex;align-items:center;gap:8px;font-size:8.4px;height:18px}
  .security-list svg{width:12px;height:12px}
  .footer{
    position:absolute;left:0;top:790px;width:596px;height:53px;
    background:linear-gradient(90deg,var(--brand-deep),var(--brand-blue) 50%,var(--brand-deep));
    color:#fff;font-family:"PT Sans",Arial,sans-serif;font-weight:700;font-size:10.5px;
  }
  .contact{position:absolute;top:18px;display:flex;align-items:center;gap:5px}
  .contact svg{width:11px;height:11px}
  .contact-email{left:24px}
  .contact-phone{left:260px}
  .contact-web{left:392px}
</style>
</head>
<body>
<div class="canvas">
  <article class="flyer">
    <svg class="header-art" viewBox="0 0 596 303" aria-hidden="false">
      <defs>
        <linearGradient id="photoTone" x1="0" y1="0" x2="1" y2="1">
          <stop offset="0" stop-color="#dfe7ef"/>
          <stop offset=".45" stop-color="var(--photo-a)"/>
          <stop offset="1" stop-color="var(--photo-b)"/>
        </linearGradient>
        <linearGradient id="heroBlue" x1="0" y1="0" x2="1" y2="1">
          <stop offset="0" stop-color="#2559c4"/>
          <stop offset="1" stop-color="#173c8f"/>
        </linearGradient>
      </defs>
      <rect x="0" y="0" width="596" height="303" fill="url(#photoTone)" role="img" aria-label="Photo of a hand turning a key in a chrome door lock in front of a white villa with a tiled roof and lawn"/>
      <polygon points="0,0 145,0 240,125 0,125" fill="#ffffff"/>
      <polygon points="240,125 268,125 380,303 355,303" fill="#3f74d6" opacity=".55"/>
      <polygon points="0,125 240,125 355,303 0,303" fill="url(#heroBlue)"/>
    </svg>

    <div class="brand-mark"><span class="dot"></span><span>Stalwart<br>Partnership</span></div>

    <h1 class="hero-title">LOCKSMITH SERVICES</h1>
    <div class="hero-rule"></div>
    <p class="hero-intro">Thank you for taking my call today, Stalwart Partnership offer all services a client may require within the Security and Locksmith industry as requested please find below more information on how we can help and support you.</p>

    <svg width="0" height="0" style="position:absolute">
      <symbol id="hex" viewBox="0 0 36 40"><polygon points="18,0 36,10 36,30 18,40 0,30 0,10" fill="#1f4fb3"/></symbol>
    </svg>

    <section class="service col-left" style="top:324px">
      <svg class="hex" viewBox="0 0 36 40"><use href="#hex"/><rect x="12" y="18" width="12" height="10" rx="1" fill="#fff"/><path d="M14 18v-3a4 4 0 0 1 8 0v3" stroke="#fff" stroke-width="2" fill="none"/></svg>
      <div class="service-body">
        <h3>Lock Outs</h3>
        <p>This service is offered 24 hours a day, 7 days a week, we are happy for your tenants to contact us directly.</p>
        <p class="price">Prices start at £65 depending on time day.</p>
      </div>
    </section>

    <section class="service col-left" style="top:415px">
      <svg class="hex" viewBox="0 0 36 40"><use href="#hex"/><path d="M9 20 18 12 27 20" stroke="#fff" stroke-width="2" fill="none"/><rect x="12" y="19" width="12" height="10" fill="#fff"/><rect x="16" y="22" width="4" height="4" fill="#1f4fb3"/></svg>
      <div class="service-body">
        <h3>Lock Changes</h3>
        <p>This service means we can change the locks in a property. We offer different packages for this dependent on what level of security lock we are changing for.</p>
        <p class="price">Prices start at £49<br>(assuming entry does not need to be gained)</p>
      </div>
    </section>

    <section class="service col-left" style="top:505px">
      <svg class="hex" viewBox="0 0 36 40"><use href="#hex"/><path d="M18 10 27 13v7c0 5-4 9-9 11-5-2-9-6-9-11v-7z" stroke="#fff" stroke-width="2" fill="none"/><rect x="15" y="19" width="6" height="5" fill="#fff"/></svg>
      <div class="service-body">
        <h3>Lock/Security Upgrades</h3>
        <p>With strategic partnerships with many lock suppliers we can offer lock upgrades including 3* and Ironclad Grade as well as adding extra locks and security devices to properties.</p>
        <p class="price">Prices quoted dependent on customer requirements.</p>
      </div>
    </section>

    <section class="service col-left" style="top:600px">
      <svg class="hex" viewBox="0 0 36 40"><use href="#hex"/><rect x="8" y="15" width="14" height="10" fill="#fff"/><path d="M22 18h4l3 3v4h-7z" fill="#fff"/><circle cx="12" cy="27" r="2" fill="#fff"/><circle cx="25" cy="27" r="2" fill="#fff"/></svg>
      <div class="service-body">
        <h3>Board Ups</h3>
        <p>Our vehicles carry all the equipment required for board up as well as a full stocked unit meaning we are available 24 hours a days 7 days a week should a customer require a property making safe after burglary or smashed window.</p>
        <p class="price">Prices Start at £70</p>
      </div>
    </section>

    <section class="service col-left" style="top:698px">
      <svg class="hex" viewBox="0 0 36 40"><use href="#hex"/><circle cx="22" cy="15" r="4" stroke="#fff" stroke-width="2" fill="none"/><path d="M19 18 10 27M13 24l2 2M11 26l2 2" stroke="#fff" stroke-width="2"/></svg>
      <div class="service-body">
        <h3>Key Cutting</h3>
        <p>We can cut all residential and commercial keys using top of the range equipment and full stocked blacks we are able to not only cut keys for existing locks but also provide extra for newly installed locks.</p>
        <p class="price">Prices dependent on customer requirement.</p>
      </div>
    </section>

    <section class="service col-right" style="top:324px">
      <svg class="hex" viewBox="0 0 36 40"><use href="#hex"/><circle cx="18" cy="20" r="4" fill="#fff"/><path d="M18 11v5M18 24v5M9 20h5M22 20h5M12 14l3 3M21 23l3 3M24 14l-3 3M15 23l-3 3" stroke="#fff" stroke-width="1.6"/></svg>
      <div class="service-body">
        <h3>Master Key Systems</h3>
        <p>Master key systems are a way for one key to open all locks on a system while still having keys that are only able to open on individual locks, perfect for office blocks where the caretaker has access to all rooms, but each tenant only has access to their own.</p>
        <p class="price">Prices quoted dependent on customer requirement.</p>
      </div>
    </section>

    <section class="service col-right" style="top:415px">
      <svg class="hex" viewBox="0 0 36 40"><use href="#hex"/><rect x="11" y="18" width="12" height="10" rx="1" fill="#fff"/><path d="M13 18v-3a4 4 0 0 1 8 0v3" stroke="#fff" stroke-width="2" fill="none"/><path d="M24 24h4v3" stroke="#fff" stroke-width="1.6" fill="none"/></svg>
      <div class="service-body">
        <h3>Keyed Alike</h3>
        <p>Keyed alike gives customers the option to have one key for all locks on a property. E.g., Front door, Back door, Garage, and padlock on out building are all operated using the same key.</p>
        <p class="price">Prices quoted dependent on customer requirement.</p>
      </div>
    </section>

    <section class="service col-right" style="top:505px">
      <svg class="hex" viewBox="0 0 36 40"><use href="#hex"/><circle cx="15" cy="14" r="3.5" stroke="#fff" stroke-width="2" fill="none"/><path d="M15 17v12M15 24h3M15 27h3" stroke="#fff" stroke-width="2"/><circle cx="23" cy="16" r="3" stroke="#fff" stroke-width="1.6" fill="none"/><path d="M23 19v9" stroke="#fff" stroke-width="1.6"/></svg>
      <div class="service-body">
        <h3>Key Holding</h3>
        <p>Mainly used as part of our security services our key holding service means we store your property keys. This reduces the cost of having locks changed if a key is lost as we can use one of our response vehicles to deliver these to you. Can also be incorporated with our lock up and unlock service and Alarm response.</p>
        <p class="price" style="margin-top:10px">Key holding costs start at less than £1 per day.</p>
      </div>
    </section>

    <aside class="security-box">
      <div class="security-tab">SECURITY SERVICES</div>
      <p class="lead"><b>MOBILE RESPONSE</b> – Stalwart Partnership use our marked vehicles to attend properties for multiple reasons.</p>
      <ul class="security-list">
        <li><svg viewBox="0 0 12 12"><path d="M3 9V6a3 3 0 0 1 6 0v3zM2 10h8" stroke="#fff" stroke-width="1.3" fill="none"/></svg>Alarm Response</li>
        <li><svg viewBox="0 0 12 12"><rect x="2.5" y="5.5" width="7" height="5.5" fill="#fff"/><path d="M4 5.5V4a2 2 0 0 1 4 0v1.5" stroke="#fff" stroke-width="1.3" fill="none"/></svg>Lock up / Unlocks</li>
        <li><svg viewBox="0 0 12 12"><path d="M6 1 10.5 2.5v3.5c0 2.5-2 4.3-4.5 5.3C3.5 10.3 1.5 8.5 1.5 6V2.5z" stroke="#fff" stroke-width="1.3" fill="none"/></svg>Security Checks</li>
      </ul>
    </aside>

    <footer class="footer">
      <div class="contact contact-email"><svg viewBox="0 0 12 12"><circle cx="6" cy="6" r="5.3" stroke="#fff" fill="none"/><rect x="3" y="4" width="6" height="4" stroke="#fff" stroke-width=".9" fill="none"/><path d="M3 4l3 2 3-2" stroke="#fff" stroke-width=".9" fill="none"/></svg>locksmith@stalwartalliance.co.uk</div>
      <div class="contact contact-phone"><svg viewBox="0 0 12 12"><circle cx="6" cy="6" r="5.3" stroke="#fff" fill="none"/><path d="M4 3.5c0 3 1.5 4.5 4.5 4.5l.5-1.2-1.3-.6-.6.6c-.9-.4-1.5-1-1.9-1.9l.6-.6-.6-1.3z" fill="#fff"/></svg>0800 562 7093</div>
      <div class="contact contact-web"><svg viewBox="0 0 12 12"><circle cx="6" cy="6" r="5.3" stroke="#fff" fill="none"/><ellipse cx="6" cy="6" rx="2.2" ry="5.3" stroke="#fff" stroke-width=".8" fill="none"/><path d="M.8 6h10.4" stroke="#fff" stroke-width=".8"/></svg>www.stalwartalliance.co.uk</div>
    </footer>
  </article>
</div>
</body>
</html>
```